Business Card Design

I need a business card design for a new business based in South West Australia.
I specialize in residential window cleaning & general handyman maintenance.

Industry/Entity Type

Business

Contact Information for Business Card

Dean Harlow - 482 SILVER HAWK DETAILING
- Window Cleaning
- House Maintenance

```html
<!DOCTYPE html>
<html lang="en">
<head>
<meta charset="utf-8">
<title>Dean Harlow – 482 Silver Hawk Detailing – Business Card</title>
<link href="https://fonts.googleapis.com/css2?family=Montserrat:wght@300;400;600&display=swap" rel="stylesheet">
<style>
  :root {
    --page-bg: #d9d6d1;
    --card-dark: #1b1c1e;
    --card-dark-edge: #2c2d30;
    --brand-cyan: #2bb8ec;
    --brand-blue: #1b6cc8;
    --band-text: #e9f8ff;
    --phone-text: #ffffff;
  }
  * { margin: 0; padding: 0; box-sizing: border-box; }
  html, body {
    width: 1200px;
    height: 900px;
    overflow: hidden;
    background: var(--page-bg);
    font-family: "Montserrat", sans-serif;
  }
  .business-card {
    position: absolute;
    left: 100px;
    top: 164px;
    width: 1000px;
    height: 572px;
    background: linear-gradient(135deg, var(--card-dark) 0%, var(--card-dark) 45%, var(--card-dark-edge) 100%);
    box-shadow: 0 18px 40px rgba(0,0,0,0.35);
    overflow: hidden;
  }
  .brand-lockup {
    position: absolute;
    left: 0;
    right: 0;
    top: 92px;
    text-align: center;
    color: var(--brand-cyan);
    font-weight: 600;
    line-height: 1;
  }
  .brand-owner {
    font-size: 44px;
    letter-spacing: 1px;
  }
  .brand-number {
    font-size: 104px;
    margin-top: 4px;
    letter-spacing: 2px;
  }
  .brand-tagline {
    font-size: 22px;
    letter-spacing: 3px;
    margin-top: 6px;
  }
  .contact-phone {
    position: absolute;
    left: 0;
    right: 0;
    top: 338px;
    display: flex;
    justify-content: center;
    align-items: center;
    gap: 14px;
    color: var(--phone-text);
    font-weight: 400;
    font-size: 30px;
    letter-spacing: 2px;
  }
  .contact-phone svg { width: 28px; height: 28px; }
  .divider-line {
    position: absolute;
    left: 0;
    right: 0;
    top: 432px;
    height: 8px;
    background: var(--brand-blue);
  }
  .services-band {
    position: absolute;
    left: 0;
    right: 0;
    top: 452px;
    bottom: 0;
    background: var(--brand-cyan);
    display: flex;
    justify-content: center;
    align-items: center;
    gap: 70px;
    color: var(--band-text);
    font-weight: 300;
    font-size: 34px;
    letter-spacing: 1px;
  }
</style>
</head>
<body>
  <main class="business-card">
    <div class="brand-lockup">
      <div class="brand-owner">DEAN HARLOW</div>
      <div class="brand-number">482</div>
      <div class="brand-tagline">SILVER HAWK DETAILING</div>
    </div>

    <div class="contact-phone">
      <svg viewBox="0 0 28 28" aria-hidden="true">
        <circle cx="14" cy="14" r="14" fill="var(--brand-cyan)"/>
        <rect x="9" y="6" width="10" height="16" rx="2" fill="none" stroke="#1b1c1e" stroke-width="2"/>
        <line x1="12" y1="19" x2="16" y2="19" stroke="#1b1c1e" stroke-width="1.5"/>
      </svg>
      <span class="phone-number">0417286540</span>
    </div>

    <div class="divider-line"></div>
    <div class="services-band">
      <span class="service">Window Cleaning</span>
      <span class="service">House Maintenance</span>
    </div>
  </main>
</body>
</html>
```